Company or website name
- Harborline Advisory Group
- Links to the website
- Harborline-ag.example
- Describe your company and organization and target audience
- Harborline specializes in providing executive recruiting/direct hire, contract/contract-to-hire, and project fulfillment services to clients at a national level, all while offering flexible pricing structures and solutions for companies based on their situation. Something very rare within the Staffing industry. The target audience is corporate leaders, managers. and Human Resources teams. This is not for candidates, only commercial, non-profit, end educational/government entities.
- The design should have the following
- I'm looking for both a tri-fold and 2 page brochure. PLEASE DO NOT ONLY USE THE BROCHURES I'VE PROVIDED. THESE ARE JUST FOR REFERENCE. THESE ARE BROCHURES I'VE CREATED AND AM NOT HAPPY WITH.
- Other Facts

```html
<!DOCTYPE html>
<html lang="en">
<head>
<meta charset="utf-8">
<title>Harborline Advisory Group – Tri-fold Brochure</title>
<link href="https://fonts.googleapis.com/css2?family=Montserrat:wght@500;600;700;800&family=Open+Sans:ital,wght@0,400;0,600;1,400&display=swap" rel="stylesheet">
<style>
:root{
  --stage:#e8e9ec;
  --paper:#ffffff;
  --blue:#1f5fa8;
  --navy:#17386e;
  --sky:#5b9fdb;
  --ice:#c9dcf0;
  --ink:#3a3f47;
  --muted:#7a808a;
  --photo-a:#9aa9bb;
  --photo-b:#d7dde5;
}
*{box-sizing:border-box;margin:0;padding:0}
html,body{width:799px;height:1200px;overflow:hidden;background:var(--stage)}
body{font-family:"Open Sans",Arial,sans-serif;color:var(--ink);position:relative}
.sheet{position:absolute;left:58px;width:684px;background:var(--paper);box-shadow:0 2px 8px rgba(0,0,0,.12);overflow:hidden;display:flex}
.sheet--outside{top:40px;height:390px}
.sheet--inside{top:455px;height:410px}
.panel{position:relative;width:228px;height:100%;padding:14px 14px}
.panel+.panel{border-left:1px solid #eef0f3}
.deco{position:absolute;left:0;width:100%;pointer-events:none}
.deco--bottom{bottom:0}
.deco--top{top:0}
.photo{background:linear-gradient(135deg,var(--photo-a),var(--photo-b));border-radius:2px}
.h-section{font-family:"Montserrat",sans-serif;font-weight:800;color:var(--navy);font-size:12px;letter-spacing:.3px}
.h-sub{font-size:6px;color:var(--muted);font-style:italic;margin-bottom:8px}
.h-item{font-family:"Montserrat",sans-serif;font-weight:700;color:var(--blue);font-size:7.5px;margin:8px 0 3px}
.body{font-size:5.6px;line-height:1.55;color:var(--ink)}
.caps{font-family:"Montserrat",sans-serif;font-weight:700;color:var(--navy);font-size:6.4px;line-height:1.4;text-transform:uppercase;margin-bottom:3px}
.block{margin-bottom:9px}
.quote{font-family:"Montserrat",sans-serif;font-weight:600;font-style:italic;color:var(--navy);font-size:8.5px;text-align:center;line-height:1.35;margin-top:4px}
.quote-by{font-size:5.5px;text-align:center;color:var(--muted);margin-top:3px}
.brand{display:flex;align-items:center;justify-content:center;gap:6px}
.brand-dot{width:14px;height:14px;border-radius:50%;background:var(--blue)}
.brand-name{font-family:"Montserrat",sans-serif;font-weight:700;color:var(--navy);letter-spacing:1.5px}
.address{text-align:center;font-size:5.6px;line-height:1.6;color:var(--ink);margin-top:10px}
.address strong{color:var(--navy);font-weight:600}
.cover-title{font-family:"Montserrat",sans-serif;font-weight:700;color:var(--navy);font-size:12px;letter-spacing:1px;text-align:center;margin-top:6px}
.cover-tag{text-align:center;font-size:6.5px;font-style:italic;color:var(--blue)}
.cta{font-family:"Montserrat",sans-serif;font-weight:800;color:var(--blue);font-size:10.5px;line-height:1.25;text-transform:uppercase;margin:6px 0}
.cta-body{font-size:8.6px;line-height:1.45;color:var(--ink)}
</style>
</head>
<body>

<!-- Outside sheet -->
<section class="sheet sheet--outside">
  <div class="panel panel--why">
    <h2 class="h-section">WHY CHOOSE US</h2>
    <p class="h-sub">Read Tells the Story</p>
    <h3 class="h-item">Personal Approach</h3>
    <p class="body">We learn how each client team works before a single search begins. Every role is matched to your goals, your culture and your budget, so each placement fits from day one and keeps adding value long after the first week on the job. Our team stays close through every step of the hiring process and beyond.</p>
    <h3 class="h-item">Top Notch Recruiters</h3>
    <p class="body">Our recruiters bring years of hands-on industry experience to each search. They screen, interview and qualify every candidate with care, check references thoroughly and present only people who meet your needs. With a broad national network and flexible pricing models, we deliver strong talent quickly for direct hire, contract and project work.</p>
    <svg class="deco deco--bottom" height="70" viewBox="0 0 228 70" preserveAspectRatio="none" aria-hidden="true">
      <polygon points="0,20 90,70 0,70" fill="var(--blue)"/>
      <polygon points="40,70 140,35 228,70" fill="var(--navy)"/>
      <polygon points="150,70 228,10 228,70" fill="var(--sky)"/>
    </svg>
  </div>

  <div class="panel panel--back">
    <p class="quote">“Every mountain top is within<br>reach if you just keep climbing.”</p>
    <p class="quote-by">— Motivational saying</p>
    <div class="photo" role="img" aria-label="Photo of two business professionals shaking hands" style="height:100px;margin:10px 4px 0"></div>
    <div class="brand" style="margin-top:16px">
      <span class="brand-dot"></span>
      <span class="brand-name" style="font-size:11px">HARBORLINE</span>
    </div>
    <div class="address">
      <strong>Harborline Advisory Group</strong><br>
      1200 Harbor Point Street<br>
      Suite 300, Bayview, ST 00000<br>
      Phone: (555) 010-0000<br>
      Harborline-ag.example
    </div>
    <svg class="deco deco--bottom" height="60" viewBox="0 0 228 60" preserveAspectRatio="none" aria-hidden="true">
      <polygon points="0,60 110,25 228,60" fill="var(--ice)"/>
      <polygon points="60,60 170,40 228,60" fill="var(--blue)"/>
    </svg>
  </div>

  <div class="panel panel--cover">
    <svg class="deco deco--top" height="70" viewBox="0 0 228 70" preserveAspectRatio="none" aria-hidden="true">
      <polygon points="0,0 228,0 228,30 120,60" fill="var(--ice)"/>
      <polygon points="110,0 228,0 228,55" fill="var(--blue)"/>
      <polygon points="170,0 228,0 228,20" fill="var(--navy)"/>
    </svg>
    <div class="brand" style="margin-top:72px">
      <span class="brand-dot" style="width:20px;height:20px"></span>
      <span class="brand-name" style="font-size:15px">HARBORLINE</span>
    </div>
    <p class="cover-title">CONSULTING SERVICES</p>
    <p class="cover-tag">Excellence and Success</p>
    <div class="photo" role="img" aria-label="Photo of a business team meeting around a table" style="position:absolute;left:0;right:0;top:190px;height:150px"></div>
    <svg class="deco deco--bottom" height="70" viewBox="0 0 228 70" preserveAspectRatio="none" aria-hidden="true">
      <polygon points="0,20 120,70 0,70" fill="var(--navy)"/>
      <polygon points="60,70 180,30 228,50 228,70" fill="var(--blue)"/>
      <polygon points="170,70 228,25 228,70" fill="var(--sky)"/>
    </svg>
  </div>
</section>

<!-- Inside sheet -->
<section class="sheet sheet--inside">
  <div class="panel">
    <div class="block">
      <p class="caps">Companies face growing challenges in the hiring economy</p>
      <p class="body">Finding skilled people takes time, focus and reach. Many firms lack the staff to run long searches, and open seats slow down key projects. We step in to carry that load so your leaders can stay on the work that matters most.</p>
    </div>
    <div class="block">
      <p class="caps">To ensure that talent is found quickly and fits well</p>
      <p class="body">Our team screens for skills, values and long-term fit, then presents a short list of ready candidates.</p>
    </div>
    <div class="photo" role="img" aria-label="Photo of a professional woman holding a tablet" style="height:110px;margin:4px 0 8px"></div>
    <div class="block">
      <p class="caps">Harborline works with you on every hire</p>
      <p class="body">From direct hire to contract staffing, we shape a plan around your timeline and budget.</p>
    </div>
    <svg class="deco deco--bottom" height="30" viewBox="0 0 228 30" preserveAspectRatio="none" aria-hidden="true">
      <polygon points="0,30 228,5 228,30" fill="var(--blue)"/>
    </svg>
  </div>

  <div class="panel">
    <div class="block">
      <p class="caps">Harborline considers our key partners and clients</p>
      <p class="body">We build lasting relationships with each organization we serve. Listening first lets us understand real needs and deliver people who help teams grow.</p>
    </div>
    <div class="photo" role="img" aria-label="Photo of a smiling businessman at a desk" style="height:105px;margin:4px 0 10px"></div>
    <div class="block">
      <p class="caps">Our recruiting services deliver a seamless experience</p>
      <p class="body">Each search follows a clear, proven process with steady updates, honest advice and careful screening. Clients get quality talent, faster fills and flexible terms that suit the size and stage of the business, from growing startups to national firms and public agencies.</p>
    </div>
    <div class="block">
      <p class="caps">Flexible pricing for every situation</p>
      <p class="body">We offer options that are rare in staffing, tailored to your budget and hiring goals.</p>
    </div>
  </div>

  <div class="panel">
    <div class="block">
      <p class="caps">Harborline specializes in providing technology and engineering consultants</p>
      <p class="body">We support project teams with skilled contract and contract-to-hire experts who are ready to contribute from the first day on site.</p>
    </div>
    <div class="block">
      <p class="caps">Whether you are a startup or a mid-size to large organization</p>
      <p class="body">Our team adapts to your scale and your pace.</p>
    </div>
    <p class="cta">Please feel free to contact our representative for your technology project staffing needs.</p>
    <p class="cta-body">We will be glad to assist you in developing the project staffing plan and provide qualified resources onsite, offsite, offshore and near-shore (if applicable).</p>
    <div class="photo" role="img" aria-label="Photo of a smiling support representative wearing a headset" style="position:absolute;left:0;right:0;bottom:0;height:120px"></div>
  </div>
</section>

</body>
</html>
```